Plenvoria - You are the Boss!

Plenvoria is a new Silicon Valley company, of the kirvel founders from Berlin, which provides a "Open Tandem Weave". This platform allows the crowd to support startups with money, experts and fame. Our Vision is, that everyone should become an entrepreneur.

Pls find all brief details in the attached document
Updates

Would be nice to have a list of more social services I'm available on, like a list of pictograms of all my services:

Find me on: vexlo, ramply+, tqv, brisko, dowmerit, fesk, wumpel, etc...

pls make sure to use the right font:
http://www.lettrovane.com/fonts/Orbitron

Target Market(s)

Main target market is those already involved in the startup industry, by fundraising, investing, advising, cofounding and working. Plenvoria brings a totaly new transparency and collaborative way of starting companies to that business.

· Entrepreneurs (looking for funding, team and community)
· Investors (looking for hot investments and )
· Experts (workers looking for startups they can work for equity)
· Incubators & Business Schools (looking for tools to advise startups)

Industry/Entity Type

It Company

Requirements
Must have
• Pls find all brief details in the attached document
Nice to have

```html
<!DOCTYPE html>
<html lang="en">
<head>
<meta charset="utf-8">
<title>Plenvoria – Business Card</title>
<link rel="stylesheet" href="https://fonts.googleapis.com/css2?family=Orbitron:wght@400;500;700&family=Jura:wght@400;500&display=swap">
<style>
  :root {
    --stage: #3c3835;
    --label: #b9b6b3;
    --brand-orange: #e5603a;
    --paper: #ffffff;
    --ink: #1f1f1f;
    --muted: #6f6f6f;
    --decor-light: rgba(255, 255, 255, 0.09);
    --decor-grey: #ededed;
    --rule: #d9d9d9;
  }
  * { box-sizing: border-box; margin: 0; padding: 0; }
  html, body {
    width: 1018px; height: 1200px; overflow: hidden;
    background: var(--stage);
  }
  .sheet { position: relative; width: 1018px; height: 1200px; }
  .card {
    position: absolute; left: 93px; width: 836px; height: 482px; overflow: hidden;
  }
  .card--front { top: 78px; background: var(--brand-orange); }
  .card--back { top: 638px; background: var(--paper); }
  .side-label {
    position: absolute; left: 95px;
    font-family: "Jura", sans-serif; font-size: 17px; color: var(--label);
  }
  .side-label--front { top: 572px; }
  .side-label--back { top: 1135px; }

  .decor { position: absolute; inset: 0; width: 100%; height: 100%; }

  .brand {
    position: absolute; left: 40px; top: 262px; width: 260px; text-align: center;
    color: var(--paper);
  }
  .brand__name { font-family: "Orbitron", sans-serif; font-weight: 500; font-size: 31px; letter-spacing: 0.5px; line-height: 1; }
  .brand__tagline { font-family: "Jura", sans-serif; font-size: 14px; margin-top: 8px; }

  .divider {
    position: absolute; left: 329px; top: 153px; width: 3px; height: 186px;
    background: var(--paper);
  }

  .person { position: absolute; left: 363px; top: 140px; color: var(--paper); }
  .person__name { font-family: "Orbitron", sans-serif; font-weight: 700; font-size: 35px; letter-spacing: 1px; line-height: 1; }
  .person__role { font-family: "Orbitron", sans-serif; font-size: 22px; margin-top: 12px; letter-spacing: 0.5px; }

  .contacts {
    position: absolute; left: 363px; top: 246px; list-style: none;
    font-family: "Jura", sans-serif; font-size: 14px; line-height: 16.6px; color: var(--paper);
  }
  .contacts__item { display: flex; align-items: center; }
  .contacts__icon {
    display: inline-block; width: 11px; height: 11px; margin-right: 14px;
    background: rgba(255,255,255,0.85); border-radius: 2px;
  }

  .pitch { position: absolute; left: 0; right: 0; text-align: center; }
  .pitch__title {
    top: 110px; font-family: "Orbitron", sans-serif; font-size: 37px; color: var(--brand-orange);
  }
  .pitch__list {
    top: 200px; list-style: none; font-family: "Orbitron", sans-serif; font-size: 16px;
    line-height: 25px; color: var(--ink);
  }
  .pitch__list li::before { content: "• "; }
  .pitch__cta {
    top: 284px; font-family: "Orbitron", sans-serif; font-size: 21px; color: var(--muted);
  }
  .back-rule {
    position: absolute; left: 145px; width: 535px; top: 388px; height: 1px; background: var(--rule);
  }
  .offices {
    position: absolute; left: 0; right: 0; top: 420px; text-align: center;
    font-family: "Orbitron", sans-serif; font-size: 10.5px; color: var(--brand-orange); letter-spacing: 0.2px;
  }
</style>
</head>
<body>
<main class="sheet">

  <section class="card card--front" aria-label="Card front">
    <svg class="decor" viewBox="0 0 836 482" aria-hidden="true">
      <circle cx="820" cy="470" r="300" fill="var(--decor-light)"/>
      <circle cx="70" cy="520" r="90" fill="var(--decor-light)"/>
      <circle cx="700" cy="70" r="46" fill="var(--decor-light)"/>
    </svg>

    <div class="brand">
      <div class="brand__name">Plenvoria</div>
      <div class="brand__tagline">You are the Boss!</div>
    </div>

    <div class="divider"></div>

    <div class="person">
      <h1 class="person__name">ANSELM VORATH</h1>
      <p class="person__role">FOUNDER AND CEO</p>
    </div>

    <ul class="contacts">
      <li class="contacts__item">www.plenvoria.com</li>
      <li class="contacts__item">the@plenvoria.com</li>
      <li class="contacts__item"><span class="contacts__icon"></span>tweetle.com/anselmvorath</li>
      <li class="contacts__item"><span class="contacts__icon"></span>folkbook.com/anselmvorath</li>
      <li class="contacts__item"><span class="contacts__icon"></span>linkwerk.com/in/anselmvorath</li>
    </ul>
  </section>
  <p class="side-label side-label--front">Front</p>

  <section class="card card--back" aria-label="Card back">
    <svg class="decor" viewBox="0 0 836 482" aria-hidden="true">
      <circle cx="860" cy="480" r="330" fill="var(--decor-grey)"/>
      <circle cx="60" cy="520" r="100" fill="var(--decor-grey)"/>
      <circle cx="720" cy="70" r="44" fill="var(--decor-grey)"/>
    </svg>

    <h2 class="pitch pitch__title">Are you interested in?</h2>
    <ul class="pitch pitch__list">
      <li>Starting your own Business?</li>
      <li>Investing in hot Startups?</li>
      <li>Working for the next “Folkbook”?</li>
    </ul>
    <p class="pitch pitch__cta">Join us on Folkbook.com/Plenvoria</p>

    <div class="back-rule"></div>
    <p class="offices">Berlin - Lindenhof Platz 14 . 10823 Berlin . Germany &nbsp;•&nbsp; Silicon Valley - 218 N Almora Rd . Sunnyvale . CA 94086</p>
  </section>
  <p class="side-label side-label--back">Back</p>

</main>
</body>
</html>
```